Tactical Supply Company needing memorable business card design

Our tactical supply comapny is in need of a new business card design that will set us apart from the amateurs. We sell tactical gear ranging from backpacks and range bags to apparel and other gear. We are looking for a sharp design that incorporates our logo, website, and name. Our colors are white, red, and black, or any combination of the three, preferably red and black.
I have attached our logo with our name underneath but I have also edited that design with the logo incorporated next to the name (attached).

Target Market(s)

Law enforcement, military, tactical

Industry/Entity Type

Business

Contact Information for Business Card

Include www.fernhollowprovisions-demo.com

Colors
000000
ec1f27
ffffff

Requirements
Must have
• Our name, logo, and website. This is intended to be a memorable simple card, no name, address, email, or phone number info is necessary. Designs that do include this additional info will still be considered if they are absolutely spectacular.
Should not have
• A standard template design, I can create that in my own on Cardvellum. I am looking for a new, creative design that is completely unique to my company.

```html
<!DOCTYPE html>
<html lang="en">
<head>
<meta charset="utf-8">
<title>Fernhollow Provisions – Business Card</title>
<link rel="stylesheet" href="https://fonts.googleapis.com/css2?family=Open+Sans:wght@400;600;700;800&display=swap">
<style>
  :root {
    --ink: #000000;
    --red: #ec1f27;
    --white: #ffffff;
    --paper-bg: #ece7df;
    --card-edge: #8a8a8a;
    --rule: #cfcfcf;
    --text-dark: #2a2a2a;
  }
  * { box-sizing: border-box; margin: 0; padding: 0; }
  html, body { width: 1167px; height: 1200px; overflow: hidden; }
  body {
    position: relative;
    background: var(--paper-bg);
    font-family: "Open Sans", Arial, sans-serif;
  }
  .card { position: absolute; width: 889px; height: 511px; overflow: hidden; }

  /* Front */
  .card-front { left: 229px; top: 65px; background: var(--ink); color: var(--white); }
  .brand-front {
    position: absolute; left: 390px; top: 62px; width: 470px;
    display: flex; align-items: center; gap: 14px;
    font-weight: 800; font-size: 38px; line-height: 1; color: var(--white);
    text-transform: uppercase; letter-spacing: 1px;
  }
  .brand-mark { width: 22px; height: 22px; background: var(--red); flex: none; }
  .holder-name { position: absolute; left: 35px; top: 238px; font-size: 31px; font-weight: 700; }
  .holder-title { position: absolute; left: 35px; top: 274px; font-size: 23px; font-weight: 700; color: var(--red); letter-spacing: 1px; }
  .title-rule { position: absolute; left: 106px; right: 0; top: 292px; height: 2px; background: var(--rule); }
  .contact-list { position: absolute; left: 35px; top: 340px; list-style: none; }
  .contact-list li { display: flex; align-items: center; gap: 10px; height: 31.5px; font-size: 21px; }
  .contact-list svg { width: 18px; height: 18px; flex: none; }
  .address { position: absolute; left: 613px; top: 400px; font-size: 21px; line-height: 35px; }
  .base-band { position: absolute; left: 0; right: 0; bottom: 0; height: 19px; background: var(--red); }

  /* Back */
  .card-back { left: 47px; top: 637px; background: var(--white); border: 1px solid var(--card-edge); }
  .brand-back {
    position: absolute; left: 0; right: 0; top: 200px;
    display: flex; justify-content: center; align-items: center; gap: 16px;
    font-weight: 800; font-size: 44px; color: var(--ink); text-transform: uppercase; letter-spacing: 1px;
  }
  .brand-back .brand-mark { width: 26px; height: 26px; }
  .site-url {
    position: absolute; left: 0; right: 0; top: 424px; text-align: center;
    font-size: 27px; letter-spacing: 3px; color: var(--text-dark);
  }
</style>
</head>
<body>

<section class="card card-front">
  <div class="brand-front"><span class="brand-mark"></span>Fernhollow Provisions</div>

  <p class="holder-name">Your Name</p>
  <p class="holder-title">Title</p>
  <div class="title-rule"></div>

  <ul class="contact-list">
    <li>
      <svg viewBox="0 0 20 20"><circle cx="10" cy="10" r="9" fill="none" stroke="#ec1f27" stroke-width="2"/><path d="M7 5l2 2-1 2 3 3 2-1 2 2-2 2c-4 0-8-4-8-8z" fill="#ec1f27"/></svg>
      012-345-6789
    </li>
    <li>
      <svg viewBox="0 0 20 20"><rect x="2" y="9" width="16" height="6" rx="1" fill="#ec1f27"/><path d="M5 9l2-4h6l2 4z" fill="#ec1f27"/><circle cx="6" cy="16" r="2" fill="#ec1f27"/><circle cx="14" cy="16" r="2" fill="#ec1f27"/></svg>
      012-345-6789
    </li>
    <li>
      <svg viewBox="0 0 20 20"><rect x="2" y="6" width="16" height="11" fill="#ec1f27"/><path d="M2 6l8 6 8-6" fill="none" stroke="#000" stroke-width="1.5"/><path d="M4 6l6-4 6 4" fill="#ec1f27"/></svg>
      info@fernhollowprovisions-demo.com
    </li>
    <li>
      <svg viewBox="0 0 20 20"><circle cx="10" cy="10" r="8" fill="none" stroke="#ec1f27" stroke-width="2"/><ellipse cx="10" cy="10" rx="3.5" ry="8" fill="none" stroke="#ec1f27" stroke-width="1.5"/><path d="M2 10h16" stroke="#ec1f27" stroke-width="1.5"/></svg>
      www.fernhollowprovisions-demo.com
    </li>
  </ul>

  <p class="address">Street Name, City Name<br>Zipcode-01234</p>
  <div class="base-band"></div>
</section>

<section class="card card-back">
  <div class="brand-back"><span class="brand-mark"></span>Fernhollow Provisions</div>
  <p class="site-url">www.fernhollowprovisions-demo.com</p>
</section>

</body>
</html>
```